SLA & Internet Advert

Advertise some of our key SLA services & Internet Connectivity services.
Service Level Agreement:
Unlimited Remote, Email, Helpdesk & Telephone Support.
Unlimited Service Calls
Support Hours Monday - Saturday 7am-10pm Sunday till 5pm
Free additional visits during quorlam periods
Free remote access to school server for staff members
Free mobile device management for tablet devices
Free Email&Webhosting Service
Remote support on every device in school allowing us to close 90% of tickets within 30 mins.
Service Level Agreement Package 1 - Includes all the above + 1 Site visit every 2 weeks £2,500 per annum
Service Level Agreement Package 2 - Includes all the above + 1 Site Visit every week £4,500 per annum
Service Level Agreement Package 3 - Includes all the above + 2 Site visits every week - £7,540 per annum
Internet Connectivity (medium/large Primary)
Managed Firewall
Managed Web filter & Safeguarding
User reporting portal/email reporting.
Main Internet Line 1000 mb/s download 100mb/s upload
Back up Internet Line 80mb/s download 20mb/s upload
100% uptime guaranteed.
£3000 per annum
Internet Connectivity (Small Primary School)
Managed Firewall
£2100 per annum
My website is https://www.varnoquell.co.uk if you need any further information like phone numbers / email address etc
Education

```html
<!DOCTYPE html>
<html lang="en">
<head>
<meta charset="utf-8">
<title>SLA &amp; Internet Connectivity Services</title>
<link href="https://fonts.googleapis.com/css2?family=Fira+Sans:wght@500;600;700&family=Open+Sans:wght@400;600&display=swap" rel="stylesheet">
<style>
:root{
  --blue:#1b5dab;
  --blue-dark:#0f3f85;
  --navy:#123a7a;
  --orange:#f07f45;
  --orange-deep:#ee6a2c;
  --sky:#cfe6f8;
  --text:#2d3440;
  --white:#ffffff;
  --bg:#e9eaec;
}
*{box-sizing:border-box;margin:0;padding:0}
html,body{width:1200px;height:1085px;overflow:hidden;background:var(--bg)}
body{font-family:"Open Sans",sans-serif;color:var(--text)}
.flyer{position:absolute;left:220px;top:0;width:760px;height:1085px;overflow:hidden;
  background:linear-gradient(180deg,var(--sky) 352px,#e6f2fb 600px,#ffffff 1000px)}
.top-band{position:absolute;left:0;top:0;width:760px;height:352px;background:var(--blue)}
.top-band-right{position:absolute;right:0;top:300px;width:80px;height:140px;background:var(--blue)}
.hero{position:absolute;left:29px;top:47px;width:692px;height:416px;border-radius:44px;
  border:6px solid var(--orange);padding:4px;background:var(--white)}
.hero-photo{width:100%;height:100%;border-radius:38px;
  background:linear-gradient(135deg,#8a5a3a 0%,#c9a27a 30%,#e9c98a 50%,#6b86b8 70%,#b99ab0 100%)}
.orange-panel{position:absolute;left:431px;top:433px;width:329px;height:652px;background:var(--orange);border-top-left-radius:44px}
.badge{position:absolute;left:589px;top:341px;width:150px;height:150px;border-radius:50%;
  background:radial-gradient(circle at 40% 35%,#2a63b3,var(--navy) 75%);
  border:3px dotted var(--white);outline:3px solid var(--navy);
  display:flex;align-items:center;justify-content:center;text-align:center;
  font-family:"Fira Sans",sans-serif;font-weight:600;font-size:16px;line-height:20px;color:var(--white)}
.headline{position:absolute;left:33px;top:510px;font-family:"Fira Sans",sans-serif;font-weight:700;
  font-size:21.5px;line-height:21px;color:var(--orange-deep)}
.pill{position:absolute;background:var(--blue);color:var(--white);font-family:"Fira Sans",sans-serif}
.sla-pill{left:18px;top:567px;width:269px;height:34px;border-radius:17px;
  font-weight:600;font-size:17px;line-height:34px;padding-left:12px;white-space:nowrap}
.bullets{position:absolute;list-style:none;font-size:13.4px;line-height:18.6px}
.bullets li{position:relative;padding-left:17px;white-space:nowrap}
.bullets li::before{content:"";position:absolute;left:0;top:4px;width:10px;height:10px;border-radius:50%;background:var(--blue)}
.bullets li::after{content:"";position:absolute;left:2.5px;top:7px;width:3px;height:3px;border-right:1.5px solid var(--white);border-top:1.5px solid var(--white);transform:rotate(45deg)}
.sla-list{left:36px;top:609px;color:var(--text)}
.net-list{color:var(--white);font-size:13.6px;line-height:19.1px}
.net-list li::before{background:#1e63b6}
.callout{position:absolute;left:35px;top:770px;font-family:"Fira Sans",sans-serif;font-weight:600;
  font-size:14.4px;line-height:19px;color:var(--blue)}
.packages{position:absolute;left:29px;top:833px;display:flex;gap:11px}
.package{width:117px;height:99px;border:1.5px dashed var(--blue);border-radius:5px;background:var(--white);text-align:center}
.package-head{background:var(--blue);color:var(--white);font-family:"Fira Sans",sans-serif;border-radius:4px 4px 0 0;padding:2px 0 3px}
.package-title{font-weight:600;font-size:11px;line-height:13px;display:block}
.package-sub{font-weight:600;font-size:6px;display:block;letter-spacing:.2px}
.package-body{font-size:7px;line-height:13px;color:var(--text);margin-top:5px}
.package-price{display:inline-block;margin-top:6px;background:var(--blue);color:var(--white);
  font-family:"Fira Sans",sans-serif;font-weight:600;font-size:10.5px;padding:2px 7px;border-radius:4px}
.package-price small,.price small{font-size:.6em;font-weight:700}
.net-pill{left:415px;width:268px;height:40px;border-radius:20px;padding-left:45px;line-height:17px;padding-top:3px}
.net-pill strong{display:block;font-weight:600;font-size:16.5px}
.net-pill span{font-family:"Open Sans",sans-serif;font-size:13px}
.net-pill svg{position:absolute;left:9px;top:7px}
.price{position:absolute;left:453px;width:125px;height:28px;background:var(--blue);color:var(--white);
  border-radius:8px 8px 0 8px;font-family:"Fira Sans",sans-serif;font-weight:600;font-size:16px;line-height:28px;padding-left:8px}
.brand{position:absolute;left:25px;top:985px;display:flex;align-items:center;gap:10px}
.brand-mark{width:34px;height:34px;background:var(--blue);border-radius:4px}
.brand-name{font-family:"Fira Sans",sans-serif;font-weight:700;font-size:34px;color:var(--blue);letter-spacing:1px;line-height:34px}
.tagline{position:absolute;left:25px;top:1032px;width:263px;border-top:1.5px solid var(--orange);padding-top:2px;
  font-family:"Fira Sans",sans-serif;font-weight:500;font-size:11.5px;letter-spacing:1.7px;color:var(--blue)}
.contact-bar{position:absolute;left:296px;top:997px;width:464px;height:54px;background:var(--blue);
  border-radius:27px 0 0 27px;display:flex;align-items:center;gap:11px;padding-left:20px;color:var(--white);
  font-size:11px;font-weight:600;white-space:nowrap}
.contact-item{display:flex;align-items:center;gap:5px;white-space:nowrap}
.contact-icon{flex:none;width:13px;height:13px;border-radius:50%;background:var(--orange);display:flex;align-items:center;justify-content:center}
</style>
</head>
<body>
<main class="flyer">
  <div class="top-band"></div>
  <div class="top-band-right"></div>
  <div class="hero"><div class="hero-photo" role="img" aria-label="Photo of a group of young pupils in a school library gathered around a tablet"></div></div>
  <div class="orange-panel"></div>
  <div class="badge">WE OFFER<br>FAST, FLEXIBLE,<br>RELIABLE<br>ICT SUPPORT</div>

  <h1 class="headline">SLA SERVICES &amp;<br>INTERNET CONNECTIVITY SERVICES</h1>
  <div class="pill sla-pill">SERVICE LEVEL AGREEMENT:</div>
  <ul class="bullets sla-list">
    <li>Unlimited Remote, Email, Helpdesk &amp; Telephone Support</li>
    <li>Unlimited Service Calls</li>
    <li>Support Hours Monday - Saturday 7am-10pm<br>Sunday till 5pm</li>
    <li>Free additional visits during quorlam periods</li>
    <li>Free remote access to school server for staff members</li>
    <li>Free mobile device management for tablet devices</li>
    <li>Free Email &amp; Webhosting Service</li>
  </ul>
  <p class="callout">Remote support on every device in school<br>allowing us to close 90% of tickets within 30 mins.</p>

  <section class="packages">
    <div class="package">
      <div class="package-head"><span class="package-title">PACKAGE 1</span><span class="package-sub">SERVICE LEVEL AGREEMENT</span></div>
      <p class="package-body">Includes all the above<br>+ 1 Site visit every 2 weeks</p>
      <span class="package-price">£2,500 <small>PER ANNUM</small></span>
    </div>
    <div class="package">
      <div class="package-head"><span class="package-title">PACKAGE 2</span><span class="package-sub">SERVICE LEVEL AGREEMENT</span></div>
      <p class="package-body">Includes all the above<br>+ 1 Site Visit every week</p>
      <span class="package-price">£4,500 <small>PER ANNUM</small></span>
    </div>
    <div class="package">
      <div class="package-head"><span class="package-title">PACKAGE 3</span><span class="package-sub">SERVICE LEVEL AGREEMENT</span></div>
      <p class="package-body">Includes all the above<br>+ 2 Site visits every week</p>
      <span class="package-price">£7,540 <small>PER ANNUM</small></span>
    </div>
  </section>

  <div class="pill net-pill" style="top:519px">
    <svg width="26" height="26" viewBox="0 0 26 26" fill="none" stroke="#fff" stroke-width="1.5"><circle cx="13" cy="13" r="11.5"/><ellipse cx="13" cy="13" rx="5" ry="11.5"/><path d="M1.5 13h23M3.5 7h19M3.5 19h19M13 1.5v23"/></svg>
    <strong>INTERNET CONNECTIVITY</strong><span>(Medium/Large Primary)</span>
  </div>
  <ul class="bullets net-list" style="left:453px;top:570px">
    <li>Managed Firewall</li>
    <li>Managed Web filter &amp; Safeguarding</li>
    <li>User reporting portal/email reporting.</li>
    <li>Main Internet Line 1000 mb/s download<br>100mb/s upload</li>
    <li>Back up Internet Line 80mb/s download<br>20mb/s upload</li>
    <li>100% uptime guaranteed</li>
  </ul>
  <div class="price" style="top:731px">£3000 <small>PER ANNUM</small></div>

  <div class="pill net-pill" style="top:792px">
    <svg width="26" height="26" viewBox="0 0 26 26" fill="none" stroke="#fff" stroke-width="1.5"><circle cx="13" cy="13" r="11.5"/><ellipse cx="13" cy="13" rx="5" ry="11.5"/><path d="M1.5 13h23M3.5 7h19M3.5 19h19M13 1.5v23"/></svg>
    <strong>INTERNET CONNECTIVITY</strong><span>(Small Primary School)</span>
  </div>
  <ul class="bullets net-list" style="left:453px;top:843px">
    <li>Managed Firewall</li>
    <li>Managed Web filter &amp; Safeguarding</li>
    <li>User reporting portal/email reporting.</li>
    <li>Main Internet Line 1000 mb/s download<br>100mb/s upload</li>
  </ul>
  <div class="price" style="top:952px">£2100 <small>PER ANNUM</small></div>

  <div class="brand"><span class="brand-mark"></span><span class="brand-name">VARNOQUELL</span></div>
  <p class="tagline">EDUCATION SUPPORT &amp; INSTALLATION</p>

  <footer class="contact-bar">
    <span class="contact-item"><span class="contact-icon"><svg width="8" height="8" viewBox="0 0 8 8"><path d="M1.5 0.5l1.5 1.5-0.8 1a4 4 0 0 0 2.8 2.8l1-0.8 1.5 1.5-1 1A6 6 0 0 1 0.5 1.5z" fill="#fff"/></svg></span>0161 555 0142</span>
    <span class="contact-item"><span class="contact-icon"><svg width="8" height="6" viewBox="0 0 8 6"><rect x="0.5" y="0.5" width="7" height="5" fill="none" stroke="#fff"/><path d="M0.5 0.5l3.5 3 3.5-3" fill="none" stroke="#fff"/></svg></span>info@varnoquell.co.uk</span>
    <span class="contact-item"><span class="contact-icon"><svg width="9" height="9" viewBox="0 0 10 10" fill="none" stroke="#fff" stroke-width="0.9"><circle cx="5" cy="5" r="4.3"/><ellipse cx="5" cy="5" rx="1.8" ry="4.3"/><path d="M0.7 5h8.6"/></svg></span>www.varnoquell.co.uk</span>
  </footer>
</main>
</body>
</html>
```